Beautiful e-comm site for 'roadside farmers stand' online!

Need a logo design and basic e-comm website (super super simple) for new business called Brindlecove. Brindlecove is an online farmers stand where local artisans can sell 'brindlecove' goods directly from their makers!

Looking for something simple, whimsicle and clean! (Ideally with a light grey or perrywinkle and some color mixed in - word 'Brindlecove' in black - can work the pear shape in somewhere but not required!)

Target Market(s)

Hobby shoppers and 'quilo' goers who want a focus on edible things and care about ingredients!

Industry/Entity Type

E-Commerce

Number of Pages Required

2 page

Font styles to use
Decorative
Script

Colors
f3f1f8
ec1f27
cadf82

Requirements
Must have
• - Basic logo
• - Homepage
• - Product Detail Page
• - Be in a responsive, woocommerce or shopify, wordpress theme (will purchase theme after design is approved)
Nice to have
• - Matching check out & cart pages
• - 'About Us' page
• - SEO plugin
Should not have
• A cluttered look/feel.

```html
<!DOCTYPE html>
<html lang="en">
<head>
<meta charset="utf-8">
<title>Brindlecove — Your online roadside farmer stand</title>
<link rel="stylesheet" href="https://fonts.googleapis.com/css2?family=Lato:wght@300;400;700;900&family=Raleway:wght@400;500;600&family=Zilla+Slab:wght@600;700&display=swap">
<style>
  :root {
    --page: #f3f1f8;
    --white: #ffffff;
    --green: #1d8a1d;
    --green-dark: #137a13;
    --green-title: #26a04a;
    --red: #ec1f27;
    --ink: #222222;
    --muted: #6b6b6b;
    --nav-text: #555555;
    --about-bg: #e9e9e9;
    --footer-bg: #0b2a0b;
    --btn-dark: #333333;
    --promo-green: #7fc47a;
    --card-border: #b9b9b9;
  }
  * { box-sizing: border-box; margin: 0; padding: 0; }
  html, body { width: 1200px; height: 2553px; overflow: hidden; }
  body { position: relative; background: var(--page); font-family: "Lato", sans-serif; color: var(--ink); }
  .abs { position: absolute; }

  /* header */
  .site-header { left: 0; top: 0; width: 1200px; height: 77px; background: var(--white); }
  .brand { left: 177px; top: 18px; display: flex; align-items: center; gap: 8px;
    font-family: "Lato", sans-serif; font-weight: 700; font-size: 30px; color: var(--ink); }
  .brand-dot { width: 14px; height: 14px; border-radius: 50%; background: var(--green-title); }
  .main-nav { left: 0; top: 0; width: 1200px; height: 77px; font-family: "Raleway", sans-serif; font-size: 13px; color: var(--nav-text); }
  .main-nav a { position: absolute; top: 22px; line-height: 21px; color: inherit; text-decoration: none; }
  .main-nav .is-active { background: var(--green); color: var(--white); border-radius: 11px; padding: 0 11px; font-weight: 600; }
  .cart-link { display: flex; align-items: center; gap: 6px; }

  /* hero */
  .hero { left: 0; top: 77px; width: 1200px; height: 527px;
    background: linear-gradient(100deg, #6f9a3a 0%, #8aa84a 30%, #7e9e3c 55%, #5f8a2e 80%, #7aa03f 100%); }
  .hero-panel { left: 0; top: 223px; width: 737px; height: 332px; background: rgba(20, 50, 15, 0.55); }
  .hero-title { left: 179px; top: 254px; font-family: "Zilla Slab", serif; font-weight: 600; font-size: 50px; color: var(--white); }
  .hero-sub { left: 179px; top: 320px; font-family: "Lato", sans-serif; font-size: 30px; letter-spacing: 1.5px; color: var(--white); }
  .hero-text { left: 179px; top: 374px; width: 440px; font-size: 14px; line-height: 23px; letter-spacing: 0.5px; color: var(--white); }
  .hero-btn { left: 179px; top: 443px; width: 131px; height: 47px; border: 2px solid var(--white);
    color: var(--white); font-weight: 900; font-size: 14px; letter-spacing: 1.5px; display: flex; align-items: center; justify-content: center; }

  /* section titles */
  .section-title { left: 0; width: 1200px; text-align: center; font-size: 30px; color: var(--green-title); font-weight: 400; }
  .section-title strong { color: #333; font-weight: 700; }

  /* products */
  .product { width: 273px; }
  .product-photo { width: 273px; height: 273px; border: 1px solid var(--card-border); }
  .product-name { margin: 10px 0 0 10px; font-size: 21px; color: var(--red); font-weight: 400; }
  .product-desc { margin: 4px 0 0 10px; width: 245px; font-size: 9.5px; line-height: 13px; color: var(--muted); }
  .product-price { margin: 12px 0 0 10px; font-size: 30px; font-weight: 700; color: var(--green-dark); }
  .add-to-cart { position: absolute; left: 0; width: 131px; height: 41px; background: var(--green);
    color: var(--white); font-size: 13px; display: flex; align-items: center; justify-content: center; }

  .divider { left: 177px; top: 1680px; width: 844px; height: 1px; background: #9a9a9a; }

  /* promos */
  .promo { top: 1714px; height: 109px; color: var(--white); overflow: hidden; }
  .promo-canned { left: 177px; width: 204px; background: linear-gradient(90deg, #5a2a2a, #8a3a3a 70%, #b05050); padding: 12px; }
  .promo-healthy { left: 391px; width: 418px; background: #252525; }
  .promo-healthy .promo-photo { position: absolute; left: 0; top: 0; width: 125px; height: 109px; background: linear-gradient(90deg, #5a4a3a, #7a5a40); }
  .promo-healthy .promo-body { position: absolute; left: 141px; top: 12px; width: 265px; }
  .promo h3 { font-size: 13px; font-weight: 700; margin-bottom: 4px; }
  .promo h3 em { font-style: normal; color: #4fc04f; font-weight: 400; }
  .promo p { font-size: 9.5px; line-height: 12px; font-weight: 700; }
  .promo .promo-link { display: inline-block; margin-top: 10px; font-size: 9.5px; text-decoration: underline; font-weight: 700; }
  .promo-shipping { left: 819px; width: 202px; background: var(--promo-green); padding: 12px 16px; color: var(--red); }
  .promo-shipping .big { font-family: "Lato", sans-serif; font-weight: 900; font-size: 34px; line-height: 34px; }
  .promo-shipping .small { font-size: 13px; font-weight: 700; }

  /* about */
  .about { left: 0; top: 1894px; width: 1200px; height: 571px; background: var(--about-bg); }
  .about-heading { left: 177px; top: 2063px; width: 262px; font-size: 14px; line-height: 23px; font-weight: 700; color: var(--ink); }
  .about-text { left: 177px; top: 2124px; width: 262px; font-size: 14px; line-height: 21px; color: #555; }
  .read-more { left: 177px; top: 2281px; width: 133px; height: 40px; background: var(--btn-dark); color: var(--white);
    border-radius: 4px; font-size: 10px; font-weight: 700; display: flex; align-items: center; justify-content: center; }
  .about-photo { left: 463px; top: 2010px; width: 558px; height: 368px;
    background: linear-gradient(180deg, #2e6b4a 0%, #4e8a3e 35%, #9a6a3a 65%, #2f8a3a 100%); }

  /* footer */
  .site-footer { left: 0; top: 2465px; width: 1200px; height: 88px; background: var(--footer-bg);
    color: #d8d8d8; font-size: 13px; display: flex; align-items: center; justify-content: center; }
</style>
</head>
<body>

<header class="site-header abs">
  <div class="brand abs"><span>Brindlecove</span><span class="brand-dot"></span></div>
  <nav class="main-nav abs">
    <a class="is-active" style="left:463px">Home</a>
    <a style="left:548px">About</a>
    <a style="left:621px">Products</a>
    <a style="left:713px">Shop</a>
    <a style="left:781px">Contact</a>
    <a style="left:866px">Login</a>
    <a class="cart-link" style="left:951px">
      <svg width="15" height="13" viewBox="0 0 15 13" aria-hidden="true"><path d="M0 1h3l2 7h8l2-6H4" fill="none" stroke="#1d8a1d" stroke-width="1.6"/><rect x="4.5" y="3" width="9" height="4" fill="#1d8a1d"/><circle cx="6" cy="11" r="1.4" fill="#1d8a1d"/><circle cx="12" cy="11" r="1.4" fill="#1d8a1d"/></svg>
      Cart (0)
    </a>
  </nav>
</header>

<section class="hero abs" role="img" aria-label="Market stall piled with fresh apples, pears and melons"></section>
<div class="hero-panel abs"></div>
<h1 class="hero-title abs">Welcome to Brindlecove</h1>
<p class="hero-sub abs">Your online roadside farmer stand</p>
<p class="hero-text abs">Canned pickles, homemade jams and jellies, homemade cookies, handmade soaps and home products, etc.</p>
<a class="hero-btn abs">SHOP NOW</a>

<h2 class="section-title abs" style="top:666px">POPULAR <strong>PRODUCTS</strong></h2>

<article class="product abs" style="left:179px; top:729px">
  <div class="product-photo" role="img" aria-label="Jar of canned pickles" style="background:radial-gradient(circle at 50% 50%, #8a9a40 0 30%, #fff 31%)"></div>
  <h3 class="product-name">Canned pickle</h3>
  <p class="product-desc">Lorem ipsum dolor sit amet, consectetur adipisicing elit, sed do eiusmod tempor incididunt ut.</p>
  <p class="product-price">$25.00</p>
  <a class="add-to-cart" style="top:393px">Add to cart</a>
</article>
<article class="product abs" style="left:463px; top:729px">
  <div class="product-photo" role="img" aria-label="Jar of strawberry jam" style="background:radial-gradient(ellipse at 50% 50%, #a0182a 0 28%, #fff 29%)"></div>
  <h3 class="product-name">Jam</h3>
  <p class="product-desc">Lorem ipsum dolor sit amet, consectetur adipisicing elit, sed do eiusmod tempor incididunt ut.</p>
  <p class="product-price">$28.00</p>
  <a class="add-to-cart" style="top:393px">Add to cart</a>
</article>
<article class="product abs" style="left:747px; top:729px">
  <div class="product-photo" role="img" aria-label="Jar of fruit jelly" style="background:radial-gradient(ellipse at 50% 50%, #c98a7a 0 30%, #fff 31%)"></div>
  <h3 class="product-name">Jellies</h3>
  <p class="product-desc">Lorem ipsum dolor sit amet, consectetur adipisicing elit, sed do eiusmod tempor incididunt ut.</p>
  <p class="product-price">$22.00</p>
  <a class="add-to-cart" style="top:393px">Add to cart</a>
</article>

<article class="product abs" style="left:179px; top:1209px">
  <div class="product-photo" role="img" aria-label="Stack of chocolate chip cookies" style="background:radial-gradient(ellipse at 50% 50%, #c08850 0 38%, #fff 39%)"></div>
  <h3 class="product-name">Homemade cookies</h3>
  <p class="product-desc">Lorem ipsum dolor sit amet, consectetur adipisicing elit, sed do eiusmod tempor incididunt ut.</p>
  <p class="product-price">$18.00</p>
  <a class="add-to-cart" style="top:393px">Add to cart</a>
</article>
<article class="product abs" style="left:463px; top:1209px">
  <div class="product-photo" role="img" aria-label="Stacked bars of handmade soap" style="background:radial-gradient(ellipse at 50% 50%, #c2a880 0 40%, #fff 41%)"></div>
  <h3 class="product-name">Homemade soaps</h3>
  <p class="product-desc">Lorem ipsum dolor sit amet, consectetur adipisicing elit, sed do eiusmod tempor incididunt ut.</p>
  <p class="product-price">$12.00</p>
  <a class="add-to-cart" style="top:393px">Add to cart</a>
</article>
<article class="product abs" style="left:747px; top:1209px">
  <div class="product-photo" role="img" aria-label="Dropper bottle of essential oil among greenery" style="background:linear-gradient(180deg, #d8ddd0 0%, #a8b890 45%, #3f6a30 100%)"></div>
  <h3 class="product-name">Grapefruit Insect repellant</h3>
  <p class="product-desc">Lorem ipsum dolor sit amet, consectetur adipisicing elit, sed do eiusmod tempor incididunt ut.</p>
  <p class="product-price">$22.00</p>
  <a class="add-to-cart" style="top:393px">Add to cart</a>
</article>

<div class="divider abs"></div>

<aside class="promo promo-canned abs" role="img" aria-label="Shelves of canned produce">
  <h3>Lots of canned products</h3>
  <p>Lorem ipsum dolor sit amet, consectetur adipisicing elit, sed do</p>
  <span class="promo-link">SHOP NOW</span>
</aside>
<aside class="promo promo-healthy abs">
  <div class="promo-photo" role="img" aria-label="Row of homemade preserve jars"></div>
  <div class="promo-body">
    <h3>Homemade products are truly <em>healthy.</em></h3>
    <p>Lorem ipsum dolor sit amet, consectetur adipisicing elit, sed do eiusmod tempor incididunt ut.</p>
    <span class="promo-link">SHOP NOW!</span>
  </div>
</aside>
<aside class="promo promo-shipping abs">
  <div class="big">FREE<br>SHIPPING</div>
  <div class="small">on orders over $99.</div>
</aside>

<section class="about abs"></section>
<h2 class="section-title abs" style="top:1954px">ABOUT <strong>US</strong></h2>
<h3 class="about-heading abs">FARMERS ROADSIDE STAND IS NOW ONLINE TO SERVE YOU.</h3>
<p class="about-text abs">Lorem ipsum dolor sit amet, consectetur adipisicing elit, sed do eiusmod tempor incididunt ut labore et dolore magna aliqua. Ut enim ad minim veniam, quis nostrud exercitation ullamco laboris nisi ut aliquip ex ea commodo consequat.</p>
<a class="read-more abs">READ MORE</a>
<div class="about-photo abs" role="img" aria-label="Roadside farm stand with striped awning and crates of vegetables"></div>

<footer class="site-footer abs">©Brindlecove All rights reserved2018</footer>

</body>
</html>
```